2 sets of Business cards, stationary/envelopes, stationary template(MS Word), door hang tag
KRV Building Works, LLC (Design A) and Steadfield Estate Holdings, LLC (Design B)
2 sets of Business cards, stationary/envelopes, stationary template(MS Word), door hang tag - Real Estate
Creative Brief
Simple
Darrel K. Winton
Managing Member
5120 Larkspur Lane, Suite B Columbia, MO 65201
Don't know yet, but need space for it
dwinton@krvbuildworks.com
www.krvbuildworks.com (Design A) and www.steadfieldleasing.com (Design B)
We are a family owned business with 90+ years in the construction and real estate sector and would like to present our company as a quality, professional organization with a sleek modern set of stationary. Stationary design A: Company name: KRV Building Works, LLC Optional Tagline: Working from experience, not for it! Color Mode: RGB color Grey :R=149 G=149 B=149 White: R=255 G=255 B=255 Black : R=0 G=0 B=0 Blue : R=0 G=97 B=240 dwinton@krvbuildworks.com (Design A) For: KRV Building Works, LLC Stationary design B: Company name: Steadfield Estate Holdings, LLC Optional Tagline: Steadfield Precision, Steadfield Dedication Color Mode: RGB color Grey :R=149 G=149 B=149 White: R=255 G=255 B=255 Black : R=0 G=0 B=0 Red : R=209 G=0 B=0 dwinton@steadfieldleasing.com (Design B) For: Steadfield Estate Holdings, LLC Phone, email, and name will change for the additional members of the company. We also want an electronic email signature, and digital stationary template (MS word). Stationary and envelopes should tie in the theme of the business cards for a uniform look. Also looking for a Header only version of the stationary, as well as a full page version (header and footer used for design).
Logo used in a creative way.
darrelkwinton darrelkwinton
Sorry, been out of the office. Waiting for partners to look at everything before making comments. We should be leaving comments and making recommendations in the next day or two for all of the designs we want to see refined. Thanks, Darrel

```html
<!DOCTYPE html>
<html lang="en">
<head>
<meta charset="utf-8">
<title>Steadfield Estate Holdings – Business Card</title>
<link href="https://fonts.googleapis.com/css2?family=Open+Sans:wght@400;600;700&display=swap" rel="stylesheet">
<style>
  :root {
    --backdrop: #1c1c1e;
    --card-white: #ffffff;
    --ink-black: #0d0d0d;
    --brand-red: #d10000;
    --brand-grey: #959595;
    --text-dark: #2a2a2a;
  }
  * { margin: 0; padding: 0; box-sizing: border-box; }
  html, body {
    width: 1200px; height: 646px; overflow: hidden;
    background: var(--backdrop);
    font-family: "Open Sans", Arial, sans-serif;
  }
  .stage { position: relative; width: 1200px; height: 646px; }
  .card {
    position: absolute; top: 180px;
    width: 500px; height: 286px;
    border-radius: 18px; overflow: hidden;
    background: var(--card-white);
  }
  .card--front { left: 70px; }
  .card--back { left: 630px; }

  .brand-mark {
    display: flex; align-items: center; gap: 10px;
  }
  .brand-mark__square {
    width: 22px; height: 22px; background: var(--brand-red);
  }
  .brand-mark__name {
    font-weight: 700; font-size: 40px; letter-spacing: 1px;
    color: var(--text-dark); line-height: 1;
  }
  .card--front .brand-mark {
    position: absolute; left: 50%; top: 50%;
    transform: translate(-50%, -50%);
  }
  .card--back .brand-mark {
    position: absolute; left: 32px; top: 106px;
  }

  .card__swoosh { position: absolute; inset: 0; }

  .holder {
    position: absolute; right: 26px; top: 22px; text-align: right;
  }
  .holder__name {
    font-weight: 700; font-size: 15px; color: var(--brand-red);
  }
  .holder__title {
    font-size: 12px; color: var(--brand-red); margin-top: 1px;
  }

  .phones {
    position: absolute; right: 26px; top: 160px; text-align: right;
    font-size: 10px; color: var(--card-white); line-height: 1.6;
  }
  .contact {
    position: absolute; left: 32px; bottom: 20px;
    font-size: 10px; color: var(--card-white); line-height: 1.55;
  }
</style>
</head>
<body>
<div class="stage">

  <section class="card card--front" aria-label="Business card front">
    <div class="brand-mark">
      <span class="brand-mark__square"></span>
      <span class="brand-mark__name">KRV</span>
    </div>
  </section>

  <section class="card card--back" aria-label="Business card back">
    <svg class="card__swoosh" width="500" height="286" viewBox="0 0 500 286" aria-hidden="true">
      <path d="M0 178 C 150 190, 330 150, 500 60 L500 286 L0 286 Z" fill="var(--brand-red)"/>
      <path d="M0 188 C 160 198, 340 168, 500 84 L500 286 L0 286 Z" fill="var(--ink-black)"/>
    </svg>

    <div class="holder">
      <p class="holder__name">Maren Holt-Vance</p>
      <p class="holder__title">Consultant</p>
    </div>

    <div class="brand-mark">
      <span class="brand-mark__square"></span>
      <span class="brand-mark__name">KRV</span>
    </div>

    <div class="phones">
      <p>P : 012 555 0148</p>
      <p>F : 012 555 0149</p>
    </div>

    <div class="contact">
      <p>mholtvance@steadfieldleasing.com</p>
      <p>www.steadfieldleasing.com</p>
      <p>5120 Larkspur Lane, Suite B Columbia</p>
    </div>
  </section>

</div>
</body>
</html>
```